Kova Festivals

We need a website that covers a website with reviews about different festivals all around the world. Should include a directory of festivals and artists as well as a nice overview of articles.

Should include
Homepage,
Directory over artists and a detail page for artists also linking them to
a directory over festivals and a detail page for each festival with different information boxes
A nice and clean article category view for possible use of sub categories from main article archive
A modern, clean and good article page

Target Market(s)

People from all over the world that travels to music festivals and enjoys to check information online and share good deals.

Industry/Entity Type

Festival

Requirements
Must have
• Review pages with boxes and spaces for information about festivals

```html
<!DOCTYPE html>
<html lang="en">
<head>
<meta charset="utf-8">
<title>Kova Festivals</title>
<link href="https://fonts.googleapis.com/css2?family=Mulish:wght@400;600&family=PT+Sans:wght@400;700&family=Noto+Serif:ital,wght@0,400;1,400&display=swap" rel="stylesheet">
<style>
:root{
  --bg-dark:#121217;
  --panel:#e9e9ea;
  --nav:#f1f1f1;
  --line:#4a4a4a;
  --accent:#f0961c;
  --text:#555;
  --text-dark:#333;
  --button:#ffc400;
  --white:#fff;
}
*{box-sizing:border-box;margin:0;padding:0}
html,body{width:1200px;height:2228px;overflow:hidden}
body{
  position:relative;
  background:
    radial-gradient(circle at 8% 45%,rgba(120,110,90,.35),transparent 18%),
    radial-gradient(circle at 92% 20%,rgba(120,120,140,.35),transparent 20%),
    radial-gradient(circle at 60% 8%,rgba(90,90,110,.4),transparent 22%),
    linear-gradient(180deg,#1b1b22,var(--bg-dark) 40%,#1a1a20);
  font-family:"PT Sans",Arial,sans-serif;color:var(--text);
}
.brand{position:absolute;left:37px;top:40px;display:flex;align-items:center;gap:16px}
.brand-mark{width:56px;height:56px;border-radius:50%;background:var(--accent)}
.brand-name{font-family:"Mulish",sans-serif;font-weight:600;font-size:36px;letter-spacing:2px;color:var(--accent)}
.social{position:absolute;left:918px;top:75px;display:flex;gap:10px}
.social span{width:27px;height:27px;border-radius:50%;border:2px solid #ddd}
.nav{position:absolute;left:30px;top:137px;width:1140px;height:63px;background:var(--nav);display:flex}
.nav a{display:flex;align-items:center;justify-content:center;font-family:"Mulish",sans-serif;font-size:16px;color:var(--text-dark);text-decoration:none;border-right:1px solid #cfcfcf;height:100%}
.panel{position:absolute;left:30px;top:224px;width:1140px;height:1895px;background:var(--panel)}
.abs{position:absolute}
.hero{left:35px;top:36px;width:1071px;height:475px;
  background:linear-gradient(180deg,#a9c6e6 0%,#cfdcea 22%,#d34b2b 45%,#e8c52a 65%,#c23a24 82%,#52535a 100%)}
.slider-dots{left:0;width:100%;top:525px;display:flex;justify-content:center;align-items:center;gap:8px}
.slider-dots .arrow{width:30px;height:30px;border-radius:50%;background:#555;display:flex;align-items:center;justify-content:center}
.slider-dots .dot{width:13px;height:13px;border-radius:50%;background:#444}
.slider-dots .dot.active{background:var(--panel);border:2px solid #444}
.quote{left:90px;width:961px;top:584px;text-align:center;font-family:"Noto Serif",serif;font-style:italic;font-size:21px;line-height:36px;color:var(--text-dark)}
.double-rule{left:35px;width:1071px;height:9px;border-top:3px solid var(--line);border-bottom:1px solid var(--line)}
.rule{left:35px;width:1071px;border-top:1px solid #777}
h2{font-family:"Mulish",sans-serif;font-weight:400;font-size:22px;color:var(--accent)}
h3{font-family:"Mulish",sans-serif;font-weight:400;font-size:19px;color:var(--accent)}
.intro{left:35px;top:793px;width:700px;font-size:15px;line-height:24px}
.checklist{left:772px;top:795px;list-style:none;font-family:"Noto Serif",serif;font-style:italic;font-weight:400;font-size:13px;line-height:24px;color:var(--text-dark)}
.checklist li::before{content:"›";font-style:normal;margin-right:14px}
.services{left:35px;top:936px;width:1071px;display:flex}
.service{width:25%;text-align:center}
.service svg{display:block;margin:0 auto 18px;height:54px}
.service p{width:226px;margin:10px auto 0;font-size:15px;line-height:24px}
.works-nav{left:1046px;top:1208px;display:flex;gap:8px}
.works-nav span{width:25px;height:25px;border-radius:50%;background:#555;display:flex;align-items:center;justify-content:center}
.works{left:35px;top:1257px;width:1071px;height:154px;overflow:hidden}
.works div{position:absolute;top:0;height:154px;width:195px}
.col{top:1524px}
.posts{left:35px;width:235px}
.post{display:flex;gap:20px;padding:12px 0;border-bottom:1px dashed #555;height:73px}
.post:last-child{border-bottom:none}
.date{width:32px;flex:none;text-align:center;font-family:"Noto Serif",serif;font-style:italic;color:var(--text-dark)}
.date b{display:block;font-weight:400;font-size:27px;line-height:26px}
.date small{font-size:12px;font-style:normal}
.post p{font-size:15px;line-height:24px}
.gallery{left:313px;width:236px}
.gallery .grid{display:grid;grid-template-columns:repeat(3,70px);gap:15px 13px;margin-top:18px}
.gallery .grid div{height:68px}
.about{left:592px;width:235px}
.about p{font-size:15px;line-height:24px;margin-top:18px}
.contact{left:870px;width:236px}
.field{display:flex;align-items:center;gap:10px;margin-top:14px}
.field:first-of-type{margin-top:18px}
.field span{width:180px;height:36px;background:var(--white);border:1px solid #ddd;border-radius:3px}
.field label{font-size:13px;color:var(--text-dark)}
.message{margin-top:14px;height:156px;background:var(--white);border:1px solid #ddd;border-radius:3px}
.submit{margin-top:14px;width:100px;height:32px;background:var(--button);color:var(--white);font-size:14px;display:flex;align-items:center;justify-content:center;border-radius:2px}
.footer{position:absolute;left:30px;top:2143px;width:1140px;height:62px;background:var(--panel);display:flex;align-items:center;justify-content:center;font-size:13px;color:var(--text-dark)}
</style>
</head>
<body>
<header>
  <div class="brand"><span class="brand-mark"></span><span class="brand-name">Kova Festivals</span></div>
  <div class="social" aria-label="Social links">
    <span style="background:#f07a1e"></span><span style="background:#3b5998"></span><span style="background:#31a9de"></span><span style="background:#333"></span><span style="background:#e8478b"></span><span style="background:#999"></span><span style="background:#3b6a8a"></span>
  </div>
  <nav class="nav">
    <a style="width:120px">Home</a><a style="width:141px">Festivals</a><a style="width:108px">Artists</a><a style="width:117px">Reviews</a><a style="width:117px">Articles</a><a style="width:137px">Contact</a>
  </nav>
</header>

<main class="panel">
  <div class="abs hero" role="img" aria-label="Street festival photo: performers in red and yellow lion dance costumes under a blue sky"></div>
  <div class="abs slider-dots">
    <span class="arrow"><svg width="10" height="12" viewBox="0 0 10 12"><path d="M7 1L2 6l5 5" stroke="#ccc" stroke-width="1.6" fill="none"/></svg></span>
    <span class="dot active"></span><span class="dot"></span><span class="dot"></span><span class="dot"></span><span class="dot"></span>
    <span class="arrow"><svg width="10" height="12" viewBox="0 0 10 12"><path d="M3 1l5 5-5 5" stroke="#ccc" stroke-width="1.6" fill="none"/></svg></span>
  </div>
  <p class="abs quote">Honest reviews of music festivals all around the world, written by fans who travel to them. Find your next festival, meet the artists and share the best deals.</p>
  <div class="abs double-rule" style="top:697px"></div>

  <h2 class="abs" style="left:35px;top:752px">Festival Guide</h2>
  <p class="abs intro">Kova Festivals collects reviews of festivals from every corner of the world. Browse the festival directory by country, month or genre and open a festival page for line-up, tickets, camping, travel and weather boxes. Every artist has a page that links to the festivals where they play, so you can follow your favourite acts from stage to stage.</p>
  <ul class="abs checklist">
    <li>Festival directory by country.</li>
    <li>Artist pages with tour dates.</li>
    <li>Reviews with rating boxes.</li>
    <li>Travel tips and shared ticket deals.</li>
  </ul>

  <div class="abs services">
    <div class="service">
      <svg viewBox="0 0 60 54" width="60"><rect x="4" y="4" width="52" height="36" rx="2" fill="#555"/><rect x="8" y="8" width="44" height="28" fill="#777"/><rect x="26" y="40" width="8" height="7" fill="#555"/><rect x="16" y="47" width="28" height="4" fill="#555"/></svg>
      <h3>Festival Directory</h3><p>Search festivals by country, date and genre with maps and line-ups.</p>
    </div>
    <div class="service">
      <svg viewBox="0 0 60 54" width="60"><rect x="14" y="2" width="26" height="6" fill="#555"/><rect x="12" y="8" width="30" height="42" rx="2" fill="#555"/><rect x="42" y="12" width="12" height="34" fill="#777"/><rect x="17" y="14" width="20" height="30" fill="#999"/></svg>
      <h3>Artist Pages</h3><p>Biographies, tour dates and links to every festival they play.</p>
    </div>
    <div class="service">
      <svg viewBox="0 0 60 54" width="60"><rect x="6" y="20" width="48" height="30" fill="#444"/><path d="M6 8l46-6 2 12-46 6z" fill="#444"/><path d="M14 7l6 10M26 5l6 10M38 4l6 10" stroke="#ddd" stroke-width="3"/></svg>
      <h3>Festival Reviews</h3><p>Rating boxes for music, crowd, food, camping and value.</p>
    </div>
    <div class="service">
      <svg viewBox="0 0 60 54" width="60"><path d="M6 2v48h50" stroke="#444" stroke-width="2" fill="none"/><path d="M12 40l12-16 10 10 16-22" stroke="#444" stroke-width="2.5" fill="none"/><circle cx="12" cy="40" r="3.5" fill="#444"/><circle cx="24" cy="24" r="3.5" fill="#444"/><circle cx="34" cy="34" r="3.5" fill="#444"/><circle cx="50" cy="12" r="3.5" fill="#444"/></svg>
      <h3>Deals &amp; Travel</h3><p>Ticket prices, travel routes and deals shared by festival fans.</p>
    </div>
  </div>

  <div class="abs rule" style="top:1163px"></div>
  <h2 class="abs" style="left:35px;top:1208px">Featured Festivals</h2>
  <div class="abs works-nav">
    <span><svg width="8" height="10" viewBox="0 0 8 10"><path d="M6 1L2 5l4 4" stroke="#ccc" stroke-width="1.5" fill="none"/></svg></span>
    <span><svg width="8" height="10" viewBox="0 0 8 10"><path d="M2 1l4 4-4 4" stroke="#ccc" stroke-width="1.5" fill="none"/></svg></span>
  </div>
  <div class="abs works">
    <div role="img" aria-label="Flower float at a parade" style="left:-74px;background:linear-gradient(180deg,#5c8a3a,#c8a030 50%,#8a8a86)"></div>
    <div role="img" aria-label="Street dancers in red costumes" style="left:144px;background:linear-gradient(180deg,#b9b6ae,#b5553a 55%,#8d8479)"></div>
    <div role="img" aria-label="Festival float with decorated performers" style="left:363px;background:linear-gradient(180deg,#3d6ea8,#d4b440 55%,#8a6a3a)"></div>
    <div role="img" aria-label="Parade procession under bunting" style="left:581px;background:linear-gradient(180deg,#c8c8d2,#b8403a 55%,#6a5a55)"></div>
    <div role="img" aria-label="Costumed dancers in green and blue" style="left:801px;background:linear-gradient(180deg,#3c7a4a,#3a5aa0 55%,#c8b8a8)"></div>
    <div role="img" aria-label="Street parade crowd" style="left:1019px;background:linear-gradient(180deg,#b8b0a8,#a84030 60%,#6a5a50)"></div>
  </div>
  <div class="abs double-rule" style="top:1459px"></div>

  <section class="abs col posts">
    <h3>Latest Reviews</h3>
    <div style="margin-top:10px">
      <div class="post"><div class="date"><b>22</b><small>JUN</small></div><p>Three days of sun at the lakeside stage</p></div>
      <div class="post"><div class="date"><b>14</b><small>MAY</small></div><p>Camping tips for first time festival goers</p></div>
      <div class="post"><div class="date"><b>11</b><small>MAY</small></div><p>The best new artists of the spring season</p></div>
      <div class="post"><div class="date"><b>08</b><small>APR</small></div><p>Cheap tickets and travel deals this summer</p></div>
    </div>
  </section>

  <section class="abs col gallery">
    <h3>Snapshots</h3>
    <div class="grid">
      <div role="img" aria-label="Festival photo" style="background:linear-gradient(#e0ddd2,#8a9a5a)"></div>
      <div role="img" aria-label="Festival photo" style="background:linear-gradient(#ece6dc,#b89a70)"></div>
      <div role="img" aria-label="Festival photo" style="background:linear-gradient(#e6dcd6,#c8a090)"></div>
      <div role="img" aria-label="Festival photo" style="background:linear-gradient(#e8d8cc,#c08060)"></div>
      <div role="img" aria-label="Festival photo" style="background:linear-gradient(#d8d0c4,#8a7050)"></div>
      <div role="img" aria-label="Festival photo" style="background:linear-gradient(#f0f0ec,#5a8a40)"></div>
      <div role="img" aria-label="Festival photo" style="background:linear-gradient(#e8e4dc,#9aa070)"></div>
      <div role="img" aria-label="Festival photo" style="background:linear-gradient(#a8c8e0,#4a7ab0)"></div>
      <div role="img" aria-label="Festival photo" style="background:linear-gradient(#f0ece4,#b0a090)"></div>
    </div>
  </section>

  <section class="abs col about">
    <h3>About</h3>
    <p>Kova Festivals is written by music fans who travel the world for live shows. We review each festival on sound, crowd, food, camping and value, so you know what to expect before you buy a ticket.</p>
    <p>Share your own review and the best deals you find with other festival fans.</p>
  </section>

  <section class="abs col contact">
    <h3>Get in Touch</h3>
    <div class="field"><span></span><label>Name*</label></div>
    <div class="field"><span></span><label>Email*</label></div>
    <div class="message"></div>
    <div class="submit">Submit</div>
  </section>
</main>

<footer class="footer">© 2013 Kova Festivals. All Right Reserved.</footer>
</body>
</html>
```